LANTERNHILL Pizza and Wraps

We need a website for a new restaurant called LANTERNHILL "PIZZA AND WRAPS".
I have attached fonts, background images, logo, images, content etc.
can provide you with what you need to get the website design done fast and easy
Updates

I have uploaded more images of the venue and some menu items. let me know if there is anything I need to provide to make your mission clear and easy

Reason: i would like a little time to provide more feedback to designers

Industry/Entity Type

Restaurant

Coding

Coded - Design and coding required

Number of Pages Required

5+ page

Colors

Designer to choose colors to be used in the design.

Requirements
Must have
• PAGES:
• Our Story
• Menu
• Reservations
• Catering & Delivery
• Contact

```html
<!DOCTYPE html>
<html lang="en">
<head>
<meta charset="utf-8">
<title>LANTERNHILL Pizza and Wraps</title>
<link href="https://fonts.googleapis.com/css2?family=Lora:wght@400;700&family=Open+Sans:ital,wght@0,400;0,600;0,700;1,400&display=swap" rel="stylesheet">
<style>
:root{
  --red:#e2222a;
  --red-bright:#ec3a40;
  --yellow:#ffe600;
  --panel:#1f1f1f;
  --black:#000;
  --white:#fff;
  --muted:#d4d4d4;
  --grey-text:#666;
  --heading:"Lora", Georgia, serif;
  --body:"Open Sans", Arial, sans-serif;
}
*{box-sizing:border-box;margin:0;padding:0}
html,body{width:1200px;height:3651px;overflow:hidden}
body{position:relative;background:var(--black);font-family:var(--body);color:var(--white)}
.abs{position:absolute}
.center{text-align:center}

/* bands */
.hero{left:0;top:0;width:1200px;height:609px;background:radial-gradient(ellipse at 40% 60%,#8a6a3a 0%,#5a4326 40%,#2a1e12 80%)}
.hero-shade{left:0;top:0;width:1200px;height:609px;background:linear-gradient(rgba(0,0,0,.35),rgba(0,0,0,.15) 60%,rgba(0,0,0,.35))}
.band-black{left:0;width:1200px;background:var(--black)}
.specials-bg{left:0;top:949px;width:1200px;height:500px;background:radial-gradient(ellipse at 60% 70%,#8c7356 0%,#5c4733 50%,#3a2c20 100%)}
.specials-shade{left:0;top:949px;width:1200px;height:500px;background:rgba(0,0,0,.35)}
.red-band{left:0;top:1911px;width:1200px;height:713px;background:radial-gradient(ellipse at 50% 50%,var(--red-bright) 0%,#d62a30 60%,#b81c22 100%)}
.contact-bg{left:0;top:3011px;width:1200px;height:640px;background:radial-gradient(ellipse at 50% 30%,#3a2a1a 0%,#1c140c 60%,#0d0906 100%)}

/* nav */
.brand{left:97px;top:40px;font-family:var(--heading);font-weight:700;font-size:42px;color:var(--red);letter-spacing:1px}
.nav{top:60px;right:100px;display:flex;gap:30px;font-family:var(--heading);font-size:15px;font-weight:700;letter-spacing:.5px}
.nav a{color:var(--white);text-decoration:none}
.nav a.active{color:var(--yellow)}

/* hero */
.hero-title{left:0;width:1200px;top:190px;font-family:var(--heading);font-weight:700;font-size:80px;letter-spacing:2px}
.hero-sub{left:0;width:1200px;top:290px;font-size:24px;font-weight:600}
.btn-outline{border:2px solid var(--white);color:var(--white);font-family:var(--heading);font-weight:700;font-size:16px;display:flex;align-items:center;justify-content:center;letter-spacing:.5px}
.dots{display:flex;gap:6px}
.dots span{width:12px;height:12px;border-radius:50%;border:2px solid var(--white)}
.dots span.on{background:var(--white)}
.dots.grey span{border-color:#999}
.dots.grey span.on{background:#999}

/* panels */
.panel{background:var(--panel);border:5px solid var(--black)}
.section-title{font-family:var(--heading);font-weight:700;font-size:36px;letter-spacing:1px;white-space:nowrap}
.copy{font-size:13px;line-height:24px;color:var(--muted)}

/* welcome */
.welcome-photo{left:134px;top:584px;width:390px;height:390px;border-radius:50%;border:5px solid var(--red);background:radial-gradient(circle at 45% 45%,#9dbb5a 0%,#6d8f3a 35%,#b44a36 70%,#3b2a1f 100%)}
.read-more{border:2px solid #888;color:var(--yellow);font-size:13px;font-weight:700;display:flex;align-items:center;justify-content:center}

/* buttons */
.btn-yellow{background:var(--yellow);color:#111;font-weight:700;font-size:15px;display:flex;align-items:center;justify-content:center}

/* menu */
.dish{border-radius:50%;border:4px solid var(--white)}
.dish-label{font-family:var(--heading);font-weight:700;font-size:16px;width:200px;text-align:center}

/* cards */
.card{background:var(--white);color:#222}
.card-photo{position:absolute;left:0;top:0;width:100%;height:187px}
.card-icon{position:absolute;left:50%;top:-37px;margin-left:-37px;width:74px;height:74px;border-radius:50%;background:var(--red);border:4px solid var(--white);display:flex;align-items:center;justify-content:center}
.card-title{position:absolute;left:0;width:100%;top:218px;font-family:var(--heading);font-weight:700;font-size:20px;text-align:center;letter-spacing:.5px}
.card-copy{position:absolute;left:30px;right:30px;top:252px;font-size:12px;line-height:22px;color:var(--grey-text);text-align:center}
.card-btn{position:absolute;left:50%;margin-left:-70px;top:353px;width:140px;height:39px;font-size:13px}

/* testimonial */
.quote-mark{font-family:var(--heading);font-weight:700;font-size:200px;line-height:1;color:var(--red)}
.quote-text{font-style:italic;font-size:14px;line-height:30px;color:var(--muted)}

/* contact */
.col-title{font-family:var(--heading);font-weight:700;font-size:15px;letter-spacing:.5px}
.label{font-size:11px;color:var(--muted)}
.field{background:var(--white)}
.info-icon{width:42px;height:42px;border-radius:50%;border:2px solid var(--red);display:flex;align-items:center;justify-content:center}
.info-text{font-size:12px;line-height:22px;color:var(--muted)}
.hours{font-size:12px;color:var(--muted);width:292px;display:flex;justify-content:space-between}
.footer-rule{left:97px;top:3568px;width:1003px;height:1px;background:#555}
.social{width:27px;height:27px;background:var(--white);border-radius:3px}
</style>
</head>
<body>

<!-- HERO -->
<div class="abs hero" role="img" aria-label="Close-up photo of a grilled chicken wrap with garlic sauce and fries"></div>
<div class="abs hero-shade"></div>
<div class="abs brand">LANTERNHILL</div>
<nav class="abs nav">
  <a class="active" href="#">HOME</a><a href="#">ABOUT</a><a href="#">MENU</a><a href="#">CATERING</a><a href="#">GALLERY</a><a href="#">CONTACT</a>
  <svg width="16" height="18" viewBox="0 0 16 16"><circle cx="6.5" cy="6.5" r="5" fill="none" stroke="#fff" stroke-width="2.2"/><line x1="10.3" y1="10.3" x2="15" y2="15" stroke="#fff" stroke-width="2.6"/></svg>
</nav>
<h1 class="abs hero-title center">PIZZA &amp; WRAPS</h1>
<p class="abs hero-sub center">At vero eos et accusamus et iusto odi</p>
<a class="abs btn-outline" style="left:501px;top:346px;width:198px;height:48px">ONLINE ORDERING</a>
<div class="abs dots" style="left:564px;top:512px"><span class="on"></span><span></span><span></span><span></span></div>

<!-- WELCOME -->
<div class="abs band-black" style="top:609px;height:340px"></div>
<div class="abs specials-bg" role="img" aria-label="Photo of hummus and shawarma plate"></div>
<div class="abs specials-shade"></div>
<section class="abs panel" style="left:97px;top:555px;width:1003px;height:443px"></section>
<div class="abs welcome-photo" role="img" aria-label="Bowl of fresh Greek salad with feta and olives"></div>
<h2 class="abs section-title" style="left:567px;top:614px;font-size:30px">WELCOME TO LANTERNHILL</h2>
<p class="abs copy" style="left:567px;top:676px;width:490px">Nam libero tempore, cum soluta nobis est eligendi optio cumque nihil imp edit quo minus id quod maxime place.</p>
<p class="abs copy" style="left:567px;top:748px;width:490px">Facere possimus, omnis voluptas assumenda est, omnis dolor repellendus autem quibusdam et aut officiis debitis aut rerum necessitatibus saepe eve niet ut et voluptates repudiandae sint et molestiae non recusanda aqueear um rerum hic tenetur a sapiente delectus.</p>
<a class="abs read-more" style="left:567px;top:888px;width:117px;height:42px">READ MORE</a>

<!-- DAILY SPECIALS -->
<h2 class="abs section-title center" style="left:0;width:1200px;top:1078px">DAILY SPECIALS</h2>
<p class="abs center" style="left:250px;width:700px;top:1146px;font-size:15px;line-height:30px;font-weight:600">Nam libero tempore, cum soluta nobis est eligendi optio cumque nihil impedit quo minus id quod maxime placeat facere possim nis voluptas assumend.</p>
<a class="abs btn-yellow" style="left:482px;top:1224px;width:238px;height:60px">CHECK OUT OUR SPECIALS</a>

<!-- BANDS BEHIND MENU PANEL -->
<div class="abs band-black" style="top:1449px;height:462px"></div>
<div class="abs red-band" role="img" aria-label="Blurred red tomato background"></div>

<!-- MENU -->
<section class="abs panel" style="left:97px;top:1387px;width:1003px;height:580px"></section>
<h2 class="abs section-title center" style="left:97px;width:1003px;top:1440px">OUR MENU</h2>
<div class="abs dish" style="left:122px;top:1552px;width:176px;height:176px;background:radial-gradient(circle,#c9b08a,#7d6650)" role="img" aria-label="Cheese pizza slices"></div>
<div class="abs dish" style="left:316px;top:1552px;width:176px;height:176px;background:radial-gradient(circle,#a85a2a,#5a2c16)" role="img" aria-label="Speciality wraps with spaghetti"></div>
<div class="abs dish" style="left:711px;top:1552px;width:176px;height:176px;background:radial-gradient(circle,#b69672,#6a5038)" role="img" aria-label="Pizza diavola"></div>
<div class="abs dish" style="left:901px;top:1552px;width:176px;height:176px;background:radial-gradient(circle,#d48a3a,#7a3a18)" role="img" aria-label="Pizza calzones"></div>
<div class="abs dish" style="left:482px;top:1521px;width:238px;height:238px;background:radial-gradient(circle at 40% 60%,#f3c648 0%,#b3542e 45%,#4a2a1a 100%);border-width:5px" role="img" aria-label="Plate of fried eggs and sausages"></div>
<div class="abs dish-label" style="left:110px;top:1748px">Cheese Pizza</div>
<div class="abs dish-label" style="left:304px;top:1748px">Speciality Wraps</div>
<div class="abs dish-label" style="left:699px;top:1748px">Pizza Diavola</div>
<div class="abs dish-label" style="left:889px;top:1748px">Pizza Calzones</div>
<div class="abs dish-label" style="left:451px;top:1793px;width:300px;font-size:17px">Wraps &amp; Syrian Pockets</div>
<p class="abs copy center" style="left:441px;top:1830px;width:320px;font-size:11px;line-height:21px">Nam libero tempore, cum soluta nobis est eligendi optio cumque nihil impedit quo minus</p>
<div class="abs dots grey" style="left:570px;top:1905px"><span class="on"></span><span></span><span></span><span></span></div>

<!-- CARDS -->
<article class="abs card" style="left:97px;top:2081px;width:317px;height:377px">
  <div class="card-photo" style="background:linear-gradient(135deg,#caa35a,#7b5a2c 60%,#3e2c18)" role="img" aria-label="Glass of iced tea with lemons"></div>
  <div class="card-icon"><svg width="34" height="28" viewBox="0 0 34 28"><rect x="2" y="2" width="30" height="24" rx="2" fill="none" stroke="#fff" stroke-width="3"/><circle cx="11" cy="10" r="3" fill="#fff"/><path d="M5 23 L14 15 L19 19 L25 12 L30 23Z" fill="#fff"/></svg></div>
  <h3 class="card-title">OUR GALLERY</h3>
  <p class="card-copy">Nam libero tempore, cum soluta nobis est eligendi optio cumque nihil impedit quo minus id quod maxime placeat facere</p>
  <a class="btn-yellow card-btn">VIEW MORE</a>
</article>
<article class="abs card" style="left:443px;top:2081px;width:314px;height:377px">
  <div class="card-photo" style="background:linear-gradient(135deg,#a89270,#6a5a44 60%,#3a3024)" role="img" aria-label="Table set with shared dishes"></div>
  <div class="card-icon"><svg width="30" height="30" viewBox="0 0 30 30"><rect x="2" y="5" width="26" height="23" rx="2" fill="none" stroke="#fff" stroke-width="3"/><line x1="2" y1="11" x2="28" y2="11" stroke="#fff" stroke-width="3"/><line x1="9" y1="1" x2="9" y2="7" stroke="#fff" stroke-width="3"/><line x1="21" y1="1" x2="21" y2="7" stroke="#fff" stroke-width="3"/><rect x="7" y="15" width="4" height="4" fill="#fff"/><rect x="13" y="15" width="4" height="4" fill="#fff"/><rect x="19" y="15" width="4" height="4" fill="#fff"/><rect x="7" y="21" width="4" height="4" fill="#fff"/><rect x="13" y="21" width="4" height="4" fill="#fff"/></svg></div>
  <h3 class="card-title">MAKE A RESERVATION</h3>
  <p class="card-copy">Nam libero tempore, cum soluta nobis est eligendi optio cumque nihil impedit quo minus id quod maxime placeat facere</p>
  <a class="btn-yellow card-btn">BOOK NOW!</a>
</article>
<article class="abs card" style="left:786px;top:2081px;width:314px;height:377px">
  <div class="card-photo" style="background:linear-gradient(135deg,#d08a4a,#9a4a22 55%,#4a2414)" role="img" aria-label="Pizza on a wooden board"></div>
  <div class="card-icon"><svg width="34" height="28" viewBox="0 0 34 28"><ellipse cx="14" cy="11" rx="12" ry="8.5" fill="none" stroke="#fff" stroke-width="3"/><path d="M7 18 L5 25 L13 19.5" fill="#fff"/><path d="M24 14 C31 15 33 20 29 23 L31 27 L25 24" fill="none" stroke="#fff" stroke-width="2.5"/></svg></div>
  <h3 class="card-title">LANTERNHILL BLOG</h3>
  <p class="card-copy">Nam libero tempore, cum soluta nobis est eligendi optio cumque nihil impedit quo minus id quod maxime placeat facere</p>
  <a class="btn-yellow card-btn">VIEW MORE</a>
</article>

<!-- TESTIMONIALS -->
<div class="abs band-black" style="top:2624px;height:387px"></div>
<div class="abs contact-bg" role="img" aria-label="Dark blurred photo of a pasta dish"></div>
<section class="abs panel" style="left:97px;top:2563px;width:1003px;height:504px"></section>
<h2 class="abs section-title center" style="left:97px;width:1003px;top:2618px">CLIENT TESTIMONIALS</h2>
<div class="abs quote-mark center" style="left:0;width:1200px;top:2690px;height:100px">&ldquo;</div>
<p class="abs quote-text center" style="left:220px;width:760px;top:2808px">" Nam libero tempore, cum soluta nobis est eligendi optio cumque nihil impedit quo minus id quod maxime placeat facere possimus, omnis voluptas assumenda est, omnis dolor repellend reporibus autem quibusdam et aut officiis debitis aut rerum necessitatibus saepe eveniet ut et voluptates repudiandae sint et molestiae "</p>
<p class="abs center" style="left:0;width:1200px;top:2926px;font-size:16px;font-weight:700">- John Doe</p>
<div class="abs dots grey" style="left:570px;top:2998px"><span class="on"></span><span></span><span></span><span></span></div>

<!-- CONTACT -->
<h2 class="abs section-title center" style="left:0;width:1200px;top:3133px">CONTACT US</h2>
<h4 class="abs col-title" style="left:97px;top:3199px">CONTACT FORM</h4>
<span class="abs label" style="left:97px;top:3240px">NAME :</span>
<span class="abs label" style="left:418px;top:3240px">PHONE NO :</span>
<div class="abs field" style="left:97px;top:3269px;width:314px;height:34px"></div>
<div class="abs field" style="left:418px;top:3269px;width:312px;height:34px"></div>
<span class="abs label" style="left:97px;top:3311px">EMAIL :</span>
<div class="abs field" style="left:97px;top:3335px;width:633px;height:34px"></div>
<span class="abs label" style="left:97px;top:3377px">MESSAGE :</span>
<div class="abs field" style="left:97px;top:3403px;width:633px;height:80px"></div>
<a class="abs btn-yellow" style="left:630px;top:3490px;width:100px;height:39px;font-size:14px">SUBMIT</a>

<h4 class="abs col-title" style="left:808px;top:3199px">CONTACT INFORMATION</h4>
<div class="abs info-icon" style="left:808px;top:3240px"><svg width="14" height="20" viewBox="0 0 14 20"><path d="M7 0C3 0 0 3 0 7c0 5 7 13 7 13s7-8 7-13C14 3 11 0 7 0z" fill="#e2222a"/><circle cx="7" cy="7" r="2.5" fill="#1c140c"/></svg></div>
<p class="abs info-text" style="left:890px;top:3240px">418 Orchard Row,<br>Maplefield</p>
<div class="abs info-icon" style="left:808px;top:3297px"><svg width="18" height="14" viewBox="0 0 18 14"><rect width="18" height="14" rx="1.5" fill="#e2222a"/><path d="M1 1 L9 8 L17 1" fill="none" stroke="#1c140c" stroke-width="1.6"/></svg></div>
<p class="abs info-text" style="left:890px;top:3307px">info@lanternhill.com</p>
<div class="abs info-icon" style="left:808px;top:3353px"><svg width="18" height="18" viewBox="0 0 18 18"><path d="M4 1 L7 5 L5 7 C6 10 8 12 11 13 L13 11 L17 14 L15 17 C8 17 1 10 1 3Z" fill="#e2222a"/></svg></div>
<p class="abs info-text" style="left:890px;top:3363px">1 555 014 2290</p>

<h4 class="abs col-title" style="left:808px;top:3423px">OPENING HOURS</h4>
<div class="abs hours" style="left:808px;top:3456px"><span>Monday -</span><span>8 Am - 12 Am</span></div>
<div class="abs hours" style="left:808px;top:3480px"><span>Tuesday, Wednesday &amp; Thursday</span><span>8 Am - 10 Pm</span></div>
<div class="abs hours" style="left:808px;top:3504px"><span>Friday &amp; Saturday</span><span>8 Am – Close</span></div>

<div class="abs footer-rule"></div>
<p class="abs" style="left:97px;top:3594px;font-size:11px;color:var(--muted)">Copyrights © 2017, Lanternhill . All Rights Reserved.</p>
<div class="abs" style="left:952px;top:3588px;display:flex;gap:13px">
  <span class="social"></span><span class="social"></span><span class="social"></span><span class="social"></span>
</div>

</body>
</html>
```